Tallowby Real Estate Yard Sign

Look to develop a real estate sign that would be place in the front yard or window of our clients. It will need to be able to be read from the road so the letter will need to be larger. The sign dimension will be 24" wide x 18" tell or 36" Wide x 24" Tall. We would like to use our house logo as the back part on the sign but we would like to see other creative options also. Our company name is Tallowby Real Estate and our web address is Tallowbyrealestate.example. A spot for our phone number will also be required in the (XXX)-XXX-XXXX format. Please utilize our logo for the aesthetic feel of the sign.
Please include our company tagline. "Where Real Estate and Real Easy Move You"
This needs to be very eye catching and appealing to buyers. We want out Blue and Orange house to be very noticeable.
"Landscape format place
Target Market(s)
24-55 year olds.
Industry/Entity Type
Real Estate
Requirements
Must have
- Please be in Landscape. The sign is wider than it is tall.
It Needs to be eye catching and noticeable.

```html
<!DOCTYPE html>
<html lang="en">
<head>
<meta charset="utf-8">
<title>Tallowby Real Estate Yard Sign</title>
<link href="https://fonts.googleapis.com/css2?family=Montserrat:wght@500;600&display=swap" rel="stylesheet">
<style>
  :root {
    --brand-blue: #1d5aa8;
    --brand-orange: #f58220;
    --sign-white: #ffffff;
  }
  * { margin: 0; padding: 0; box-sizing: border-box; }
  html, body {
    width: 1200px;
    height: 800px;
    overflow: hidden;
    background: var(--sign-white);
  }
  .yard-sign {
    position: relative;
    width: 1200px;
    height: 800px;
    background: var(--sign-white);
    font-family: "Montserrat", sans-serif;
    overflow: hidden;
  }
  .roofline {
    position: absolute;
    inset: 0;
    width: 1200px;
    height: 800px;
  }
  .roofline polygon { fill: var(--brand-orange); }
  .brand {
    position: absolute;
    left: 76px;
    top: 64px;
    display: flex;
    align-items: center;
    gap: 30px;
  }
  .brand-square {
    width: 150px;
    height: 146px;
    border-radius: 14px;
    background: var(--brand-orange);
  }
  .brand-name {
    font-size: 54px;
    font-weight: 600;
    color: var(--brand-blue);
    letter-spacing: -0.5px;
    white-space: nowrap;
  }
  .tagline {
    position: absolute;
    right: 90px;
    top: 386px;
    text-align: right;
    color: var(--sign-white);
    font-size: 67px;
    font-weight: 500;
    line-height: 82px;
    letter-spacing: 0.3px;
    white-space: nowrap;
  }
  .phone-number {
    position: absolute;
    left: 0;
    width: 1200px;
    top: 580px;
    text-align: center;
    color: var(--sign-white);
    font-size: 162px;
    font-weight: 500;
    line-height: 162px;
    letter-spacing: 1px;
    white-space: nowrap;
  }
</style>
</head>
<body>
  <main class="yard-sign">
    <svg class="roofline" viewBox="0 0 1200 800" aria-hidden="true">
      <polygon points="0,540 519,265 648,336 987,147 1200,262 1200,800 0,800"/>
    </svg>

    <div class="brand">
      <span class="brand-square" aria-hidden="true"></span>
      <span class="brand-name">Tallowby Real Estate</span>
    </div>

    <p class="tagline">Where Real Estate &amp;<br>Real Easy Move You!</p>

    <p class="phone-number">1800 555 019</p>
  </main>
</body>
</html>
```